Hi Designers,

I will need 4 web pages designed. The web page looks like an App (if you click on the logo, or the icon on an iPad, it will take you to the website), but it is still a webpage.

Please check the attachment on this brief to understand what specific pages I need to be designed.

A .PSD (straight-up PhotoShop image) as final deliverable is fine, as long as you give us the exact “web color numbers”.

The design is for desktop and iPad but in a single unified web application, NOT separate web app and (native) iPad app.

Details:

Brightwell Ledger Advisory Group is developing a browser-based application for use on any mobile device or desktop. The app will be used by corporations to communicate with their employees regarding legal, regulatory and company requirements for conducting business. The app is known as “Harbor Rulebook Hub.” When the user clicks on the icon for Harbor Rulebook Hub, they will enter a site full of information that a company deems necessary for the employee to do his/her job. There are several content sections within the site, including a login page, training, policies, forms, news feeds and blogs.

The application has been built using Microsoft .NET, and fully supports CSS-type skinning; it uses traditional page layouts. We are seeking a product logo concept (image), a master application/desktop icon (image), as well as a full color scheme/theme/skin design for all areas of the application (header area, body text, menu bar, etc.) in the form of a CSS. The look should be clean, crisp and professional; nothing cartoony or whimsical. It should be easy to read and “airy”.

We have sketched prototypes for the basic application page layout that we can send as a next step of the process.
Updates

Screen shots have been uploaded to this project.  Please use them to guide your design.

Dear designers,

I apologize for the delay in providing feedback. My partners and I will provide feedback in a few days. Thank you for your patience.

Industry/Entity Type

Business

Font styles to use
Other font styles liked:
• see font on screen shots when uploaded

```html
<!DOCTYPE html>
<html lang="en">
<head>
<meta charset="utf-8">
<title>Harbor Rulebook Hub</title>
<link rel="stylesheet" href="https://fonts.googleapis.com/css2?family=Open+Sans:ital,wght@0,400;0,600;0,700;1,400&family=Roboto:wght@300;400&display=swap">
<style>
:root{
  --bar-top:#45484d;
  --bar-bottom:#2b2d31;
  --bar-text:#ffffff;
  --bar-divider:#1c1d20;
  --badge:#e8472f;
  --page-bg:#f1efea;
  --side-bg:#f6f9fb;
  --line:#dfe3e6;
  --text:#333333;
  --muted:#666666;
  --soft:#8a8a8a;
  --icon:#b7b9bb;
  --link:#3f78b5;
  --accent:#d9403a;
  --mark:#6b3a5c;
  --card:#ffffff;
  --card-head:#f1f1f1;
  --row-alt:#ececec;
  --social:#8d99a6;
}
*{box-sizing:border-box;margin:0;padding:0}
html,body{width:1200px;height:748px;overflow:hidden}
body{position:relative;background:var(--page-bg);font-family:"Open Sans",Arial,sans-serif;color:var(--text)}

/* top bar */
.topbar{position:absolute;left:0;top:0;width:1200px;height:44px;background:linear-gradient(var(--bar-top),var(--bar-bottom));color:var(--bar-text);font-size:12px;font-weight:600}
.nav-item{position:absolute;top:0;height:44px;display:flex;align-items:center;gap:8px}
.nav-item svg{width:14px;height:14px}
.nav-home{left:25px;width:99px;padding-left:10px;background:#232528}
.badge{width:16px;height:16px;border-radius:50%;background:var(--badge);font-size:9px;display:flex;align-items:center;justify-content:center;font-weight:700}
.nav-divider{position:absolute;top:8px;width:1px;height:28px;background:var(--bar-divider)}
.top-search{position:absolute;left:454px;top:10px;width:176px;height:26px;border-radius:6px;background:#1f2124;display:flex;align-items:center;gap:14px;padding-left:10px;font-weight:400;font-size:12px}
.user{position:absolute;right:26px;top:0;height:44px;display:flex;align-items:center;gap:10px;font-size:11.5px;line-height:13px}
.avatar{width:29px;height:29px;border:2px solid #ddd;background:linear-gradient(#c9a58a,#7d6a5c)}

/* sidebar */
.sidebar{position:absolute;left:0;top:44px;width:212px;height:685px;background:var(--side-bg);border-right:1px solid var(--line)}
.side-title{position:absolute;left:12px;top:15px;font-size:11px;font-weight:700}
.side-search{position:absolute;left:9px;top:41px;width:176px;height:24px;border:2px solid #e4e6e8;border-radius:8px;background:#fff;display:flex;align-items:center;gap:10px;padding-left:8px;font-size:11px;color:#aaa}
.side-menu{position:absolute;left:0;top:85px;width:211px;list-style:none}
.side-menu li{height:45.5px;border-bottom:1px solid var(--line);display:flex;align-items:center;gap:13px;padding-left:10px;font-size:11.5px;font-weight:600;color:var(--muted)}
.side-menu li:last-child{border-bottom:1px solid #cfd3d6}
.side-menu svg{width:26px;height:24px;fill:var(--icon)}
.signin{position:absolute;left:13px;top:466px}
.signin h2{font-size:21px;font-weight:400;color:#444}
.signin p{margin-top:12px;font-size:13px;color:#444}
.register{position:absolute;left:13px;top:539px;width:190px;height:34px;border:1px solid var(--line);background:#fff;font-size:11.5px;color:var(--muted);display:flex;align-items:center;padding-left:5px}
.socials{position:absolute;left:16px;top:581px;display:flex;gap:16px}
.socials span{width:28px;height:28px;border-radius:50%;background:var(--social)}
.copyright{position:absolute;left:10px;top:637px;font-size:10px;font-weight:600;color:var(--muted)}

/* welcome */
.welcome{position:absolute;left:250px;top:44px;width:940px;height:112px;background:#fbfbfb;border:1px solid #d8d8d8;border-top:none}
.welcome-icon{position:absolute;left:15px;top:16px;width:22px;height:21px;background:#dedede;border:1px solid #cfcfcf}
.welcome h1{position:absolute;left:43px;top:17px;font-size:13.5px;font-weight:700}
.welcome p{position:absolute;left:43px;top:36px;width:880px;font-family:Roboto,Arial,sans-serif;font-weight:300;font-size:11.7px;line-height:19px;color:#555}
.welcome a,.more{color:var(--accent);text-decoration:none}
.stats{position:absolute;right:26px;top:86px;display:flex;gap:28px;font-family:Roboto,Arial,sans-serif;font-weight:300;font-size:13px;color:#555}
.stats span{display:flex;align-items:center;gap:10px}
.stats svg{width:18px;height:15px;fill:#bfbfbf}

/* section heads */
.section-head{position:absolute;top:170px;font-size:12.5px;display:flex;align-items:center;gap:7px}
.section-head i{width:11px;height:7px;background:
  radial-gradient(circle,var(--mark) 1.4px,transparent 1.5px) 0 0/4px 3.5px}

.card{position:absolute;background:var(--card);box-shadow:0 0 3px rgba(0,0,0,.22)}
.card-head{height:28px;background:linear-gradient(#f7f7f7,#ececec);border-bottom:1px solid #ddd;font-size:11.5px;font-weight:600;display:flex;align-items:center;padding-left:8px}
.thumb{position:absolute;width:42px;height:42px}
.thumb.grass{background:linear-gradient(#8aa46a,#3f6b2c)}
.thumb.crowd{background:linear-gradient(#7c98b8,#4f6b3e)}
.thumb.person{background:linear-gradient(#b8957a,#5b4a44)}

.post{position:relative;height:100px}
.post .thumb{left:4px;top:10px}
.post h3{position:absolute;left:52px;top:18px;font-size:12px;font-weight:400;color:var(--link);text-decoration:underline}
.post p{position:absolute;left:8px;top:36px;width:314px;text-indent:44px;font-size:9.6px;line-height:13.5px;color:#444}
.post time{position:absolute;right:16px;bottom:8px;font-size:9px;font-style:italic;color:var(--soft);display:flex;gap:3px;align-items:center}
.post time svg{width:10px;height:10px}

.game-list{padding:4px 12px 0 10px}
.game-item{position:relative;height:61px;margin-bottom:6px;border:1px solid #dcdcdc;background:#fff}
.game-item .thumb{left:4px;top:6px}
.game-item p{position:absolute;left:50px;top:5px;width:250px;font-size:10px;line-height:17px;color:#444}

.board{width:100%;border-collapse:collapse;font-size:10px}
.board th{height:30px;text-align:left;font-size:11.5px;font-weight:600;padding-left:12px;background:linear-gradient(#f7f7f7,#ececec);border-bottom:1px solid #ddd;border-top:8px solid #fff}
.board td{height:38.6px;padding-left:12px;color:var(--soft)}
.board td.num{font-weight:600;color:#333;font-size:9px;padding-left:6px}
.board tr:nth-child(even) td{background:var(--row-alt)}
</style>
</head>
<body>

<header class="topbar">
  <div class="nav-item nav-home">
    <svg viewBox="0 0 14 14"><path d="M1 10a6 6 0 0 1 12 0z" fill="#fff"/></svg>Home<span class="badge">3</span>
  </div>
  <div class="nav-item" style="left:145px"><svg viewBox="0 0 14 14" fill="#fff"><rect x="1" y="1" width="12" height="12" fill="none" stroke="#fff" stroke-width="1.5"/><rect x="3" y="4" width="8" height="1.5"/><rect x="3" y="7" width="8" height="1.5"/><rect x="3" y="10" width="8" height="1.5"/></svg>Menu</div>
  <span class="nav-divider" style="left:223px"></span>
  <div class="nav-item" style="left:247px"><svg viewBox="0 0 14 14"><rect x="1" y="2" width="11" height="11" fill="none" stroke="#fff" stroke-width="1.6"/><path d="M6 8l7-7" stroke="#fff" stroke-width="1.6"/></svg>Hcp 360</div>
  <span class="nav-divider" style="left:330px"></span>
  <div class="nav-item" style="left:348px"><svg viewBox="0 0 14 14" stroke="#fff" stroke-width="1.5"><path d="M3 1v12M7 1v12M11 1v12"/><path d="M1 5h4M5 9h4M9 4h4"/></svg>Game</div>
  <span class="nav-divider" style="left:429px"></span>
  <div class="top-search"><svg viewBox="0 0 14 14" width="13" height="13"><circle cx="6" cy="6" r="4.5" fill="none" stroke="#888" stroke-width="1.6"/><path d="M9.5 9.5l3.5 3.5" stroke="#888" stroke-width="1.8"/></svg>Search...</div>
  <div class="user">
    <svg viewBox="0 0 24 20" width="24" height="20" fill="#fff"><path d="M1 19h22v-2H1zM3 16h2V7H3zM7 16h2V5H7zM11 16h2V3h-2zM15 16h2V5h-2zM19 16h2V7h-2z"/></svg>
    <span>Corin<br>Vale</span>
    <span class="avatar" role="img" aria-label="User profile photo"></span>
  </div>
</header>

<aside class="sidebar">
  <div class="side-title">INDUSTRY NEWS</div>
  <div class="side-search"><svg viewBox="0 0 14 14" width="13" height="13"><circle cx="6" cy="6" r="4.5" fill="none" stroke="#333" stroke-width="1.8"/><path d="M9.5 9.5l3.5 3.5" stroke="#333" stroke-width="2"/></svg>Search...</div>
  <ul class="side-menu">
    <li><svg viewBox="0 0 26 24"><circle cx="13" cy="6" r="5"/><path d="M3 24a10 10 0 0 1 20 0z"/></svg>Compliance News</li>
    <li><svg viewBox="0 0 26 24"><ellipse cx="10" cy="10" rx="9" ry="6"/><ellipse cx="17" cy="14" rx="8" ry="5"/></svg>Docementry</li>
    <li><svg viewBox="0 0 26 24"><circle cx="9" cy="10" r="4"/><path d="M1 24a8 8 0 0 1 16 0z"/><ellipse cx="20" cy="5" rx="5" ry="4"/></svg>Compliance Blog</li>
    <li><svg viewBox="0 0 26 24"><rect x="12" y="4" width="10" height="3"/><rect x="12" y="9" width="10" height="3"/><rect x="12" y="14" width="10" height="3"/><circle cx="6" cy="19" r="4"/><rect x="12" y="19" width="12" height="3"/></svg>Relevant Links</li>
    <li><svg viewBox="0 0 26 24"><path d="M2 2v20h22" fill="none" stroke="#b7b9bb" stroke-width="2"/><path d="M4 18l6-7 5 4 8-9" fill="none" stroke="#b7b9bb" stroke-width="2"/></svg>Graphics</li>
    <li><svg viewBox="0 0 26 24"><path d="M13 2L1 12h3v11h6v-7h6v7h6V12h3z"/></svg>Home</li>
    <li><svg viewBox="0 0 26 24"><path d="M13 2a6 6 0 0 1 6 6v8l3 4H4l3-4V8a6 6 0 0 1 6-6z"/><circle cx="13" cy="22" r="2"/></svg>Reports</li>
    <li><svg viewBox="0 0 26 24"><circle cx="13" cy="12" r="11"/><path d="M6 6c3 2 4 5 2 8M15 3c1 4 5 5 7 6M12 22c0-4 4-6 6-5" stroke="#f6f9fb" stroke-width="1.5" fill="none"/></svg>Media Value</li>
  </ul>
  <div class="signin">
    <h2>Sign In</h2>
    <p>Just select your favorite social</p>
  </div>
  <div class="register">Register here</div>
  <div class="socials" aria-label="Social sign-in options"><span></span><span></span><span></span><span></span></div>
  <div class="copyright">© &nbsp;2013 All Rights Reserved.</div>
</aside>

<section class="welcome">
  <span class="welcome-icon"></span>
  <h1>WELCOME TO THE HARBOR RULEBOOK HUB</h1>
  <p>Lorem Ipsum is simply dummy text of the printing and typesetting industry. Lorem Ipsum has been the industry's standard dummy text ever since the 1500s, when an unknown printer took a galley of type and scrambled it to make a type specimen book. It has survived not only five centuries, but also the leap into electronic typesetting... <a href="#">Read more</a></p>
  <div class="stats">
    <span><svg viewBox="0 0 18 15"><path d="M1 5v9h14v-4h-2v2H3V7h3V5z"/><path d="M10 1l6 4-6 4V7c-3 0-5 1-6 3 0-4 2-6 6-6z"/></svg>569 Shares</span>
    <span><svg viewBox="0 0 18 15"><path d="M9 2C4 2 1 7.5 1 7.5S4 13 9 13s8-5.5 8-5.5S14 2 9 2zm0 9a3.5 3.5 0 1 1 0-7 3.5 3.5 0 0 1 0 7z"/></svg>3,152 Views</span>
    <span><svg viewBox="0 0 18 15"><path d="M9 1C4.5 1 1 3.7 1 7c0 1.7 1 3.2 2.5 4.3L2 14l4-2c1 .3 2 .4 3 .4 4.5 0 8-2.7 8-5.9S13.5 1 9 1z"/></svg>21 Comments</span>
  </div>
</section>

<div class="section-head" style="left:248px"><i></i>What is new.?</div>
<div class="section-head" style="left:608px"><i></i>Compliance Game Center</div>
<div class="section-head" style="left:978px"><i></i>Leader Board</div>

<!-- dashboard posts -->
<article class="card" style="left:250px;top:194px;width:324px;height:132px">
  <div class="card-head">Dash Board</div>
  <div class="post">
    <span class="thumb person" role="img" aria-label="Photo of a smiling employee"></span>
    <h3>Code of Conduct Certification</h3>
    <p>Plusieurs variations de Lorem Ipsum peuvent être trouvées ici ou là, mais la majeure partie d'entre elles a été altérée par trouvées ialtérée par.</p>
    <time><svg viewBox="0 0 10 10"><rect x=".5" y="1.5" width="9" height="8" fill="none" stroke="#999"/><path d="M.5 4h9" stroke="#999"/></svg>March 21st , 2013</time>
  </div>
</article>
<article class="card" style="left:251px;top:347px;width:324px;height:111px">
  <div class="post">
    <span class="thumb grass" role="img" aria-label="Photo of people sitting on a lawn"></span>
    <h3>Code of Conduct Certification</h3>
    <p>Plusieurs variations de Lorem Ipsum peuvent être trouvées ici ou là, mais la majeure partie d'entre elles a été altérée par trouvées ialtérée par.</p>
    <time><svg viewBox="0 0 10 10"><rect x=".5" y="1.5" width="9" height="8" fill="none" stroke="#999"/><path d="M.5 4h9" stroke="#999"/></svg>March 21st , 2013</time>
  </div>
</article>
<article class="card" style="left:250px;top:478px;width:324px;height:111px">
  <div class="post">
    <span class="thumb crowd" role="img" aria-label="Photo of a group at an outdoor event"></span>
    <h3>Code of Conduct Certification</h3>
    <p>Plusieurs variations de Lorem Ipsum peuvent être trouvées ici ou là, mais la majeure partie d'entre elles a été altérée par trouvées ialtérée par.</p>
    <time><svg viewBox="0 0 10 10"><rect x=".5" y="1.5" width="9" height="8" fill="none" stroke="#999"/><path d="M.5 4h9" stroke="#999"/></svg>March 21st , 2013</time>
  </div>
</article>
<article class="card" style="left:250px;top:607px;width:324px;height:122px">
  <div class="post">
    <span class="thumb grass" role="img" aria-label="Photo of people relaxing on grass"></span>
    <h3>Code of Conduct Certification</h3>
    <p>Plusieurs variations de Lorem Ipsum peuvent être trouvées ici ou là, mais la majeure partie d'entre elles a été altérée par trouvées ialtérée par.</p>
  </div>
</article>

<!-- game center -->
<section class="card" style="left:613px;top:194px;width:325px;height:535px">
  <div class="card-head" style="padding-left:14px">Know you way Around the center</div>
  <div class="game-list">
    <div class="game-item"><span class="thumb grass" role="img" aria-label="Photo of students on a lawn"></span><p>Lorem Ipsum is simply dummy text of the pext ever since the 1500s, when an unknown printer took a g <span class="more">Read more</span></p></div>
    <div class="game-item"><span class="thumb crowd" role="img" aria-label="Photo of a crowd at an event"></span><p>Lorem Ipsum is simply dummy text of the pext ever since the 1500s, when an unknown printer took a g <span class="more">Read more</span></p></div>
    <div class="game-item"><span class="thumb grass" role="img" aria-label="Photo of people on a field"></span><p>Lorem Ipsum is simply dummy text of the pext ever since the 1500s, when an unknown printer took a g <span class="more">Read more</span></p></div>
    <div class="game-item"><span class="thumb grass" role="img" aria-label="Photo of a campus lawn"></span><p>Lorem Ipsum is simply dummy text of the pext ever since the 1500s, when an unknown printer took a g <span class="more">Read more</span></p></div>
    <div class="game-item"><span class="thumb grass" role="img" aria-label="Photo of a group sitting outdoors"></span><p>Lorem Ipsum is simply dummy text of the pext ever since the 1500s, when an unknown printer took a g <span class="more">Read more</span></p></div>
    <div class="game-item"><span class="thumb person" role="img" aria-label="Photo of a smiling employee"></span><p>Lorem Ipsum is simply dummy text of the pext ever since the 1500s, when an unknown printer took a g <span class="more">Read more</span></p></div>
    <div class="game-item"><span class="thumb grass" role="img" aria-label="Photo of people on grass"></span><p>Lorem Ipsum is simply dummy text of the pext ever since the 1500s, when an unknown printer took a g <span class="more">Read more</span></p></div>
  </div>
</section>

<!-- leader board -->
<section class="card" style="left:978px;top:199px;width:212px;height:530px;overflow:hidden">
  <table class="board">
    <thead><tr><th>Board</th><th style="padding-left:6px">Price</th><th style="padding-left:8px">Date</th></tr></thead>
    <tbody>
      <tr><td>New Events</td><td class="num">$320</td><td class="num">23 Jul 2013</td></tr>
      <tr><td>Archive</td><td class="num">$115</td><td class="num">10 Aug 2013</td></tr>
      <tr><td>Notes Stories</td><td class="num">$45</td><td class="num">15 Sep 2013</td></tr>
      <tr><td>Database</td><td class="num">$4,200</td><td class="num">30 Oct 2013</td></tr>
      <tr><td>Schedule</td><td class="num">$1,050</td><td class="num">1 Nov 2013</td></tr>
      <tr><td>New Events</td><td class="num">$320</td><td class="num">23 Jul 2013</td></tr>
      <tr><td>Archive</td><td class="num">$115</td><td class="num">10 Aug 2013</td></tr>
      <tr><td>Notes Stories</td><td class="num">$45</td><td class="num">15 Sep 2013</td></tr>
      <tr><td>Database</td><td class="num">$4,200</td><td class="num">30 Oct 2013</td></tr>
      <tr><td>Schedule</td><td class="num">$1,050</td><td class="num">1 Nov 2013</td></tr>
      <tr><td>New Events</td><td class="num">$320</td><td class="num">23 Jul 2013</td></tr>
      <tr><td>Archive</td><td class="num">$115</td><td class="num">10 Aug 2013</td></tr>
      <tr><td>Notes Stories</td><td class="num">$45</td><td class="num">15 Sep 2013</td></tr>
    </tbody>
  </table>
</section>

</body>
</html>
```